Car Design - New van

It's Marisol and Tom from Larkin the Plumber.

Below is the vehicle - it is a Rovanta Kesslo. I have another company with the type of look we are chasing with your creative flair thrown in.

* We would like the Larkin the Plumber Logo to be as large as possible
on the side of the van along with the phone numbers

* The back of the van we would like the logo to be as large as possible with the phone numbers.

* We would like the Larkin the plumber web address www.larkintheplumber.com.au to be placed along bottom of vehicle as per the previous trucks. And of course phone numbers to be as large as possible without over bearing.

thanks
Marisol

```html
<!DOCTYPE html>
<html lang="en">
<head>
<meta charset="utf-8">
<title>Larkin the Plumber – Van Wrap</title>
<link rel="stylesheet" href="https://fonts.googleapis.com/css2?family=Exo+2:wght@500;600;700&family=Oswald:wght@600&display=swap">
<style>
  :root {
    --wrap-white: #efefed;
    --wrap-black: #0b0b0b;
    --bg: #ffffff;
    --bullet: #2b4fa3;
  }
  html, body { margin: 0; padding: 0; overflow: hidden; background: var(--bg); }
  .canvas { width: 799px; height: 1200px; display: block; }
  .panel-white { fill: var(--wrap-white); stroke: #cfcfcc; stroke-width: 1; }
  .panel-black { fill: var(--wrap-black); }
  .swoosh-rule { fill: none; stroke: var(--wrap-black); stroke-width: 3; }
  .arch { fill: var(--bg); }
  .logo-ring { fill: #ffffff; stroke: var(--wrap-black); stroke-width: 3; }
  .logo-name { font-family: "Exo 2", sans-serif; font-weight: 700; fill: var(--wrap-black); text-anchor: middle; letter-spacing: 1px; }
  .front .logo-name { letter-spacing: 0; }
  .service { font-family: "Exo 2", sans-serif; font-weight: 600; fill: var(--wrap-black); font-size: 11px; text-transform: uppercase; }
  .bullet { fill: var(--bullet); }
  .web-address { font-family: "Oswald", sans-serif; font-weight: 600; fill: var(--wrap-black); font-size: 23px; }
  .slogan { font-family: "Exo 2", sans-serif; font-weight: 600; fill: #ffffff; font-size: 20px; text-anchor: middle; }
  .area-label { font-family: "Exo 2", sans-serif; font-weight: 500; fill: #ffffff; font-size: 12.5px; }
  .area-number { font-family: "Exo 2", sans-serif; font-weight: 600; fill: #ffffff; font-size: 14.5px; letter-spacing: .5px; }
  .area-divider { stroke: #ffffff; stroke-width: 1.5; }
  .back .area-label { font-size: 10px; }
  .back .area-number { font-size: 11px; letter-spacing: 0; }
  .back .service { font-size: 9.5px; }
</style>
</head>
<body>
<svg class="canvas" viewBox="0 0 799 1200" xmlns="http://www.w3.org/2000/svg">

  <!-- Side panel, driver side (front at left) -->
  <g class="side side-left">
    <path class="panel-white" d="M30,322 Q30,286 62,272 L172,236 Q232,190 302,160 Q324,148 362,146 L690,146 Q712,146 714,170 L718,395 L42,395 Q28,395 28,380 Z"/>
    <path class="panel-black" d="M212,334 L522,334 Q536,334 546,320 L592,254 Q600,242 614,242 L716,242 L718,395 L212,395 Z"/>
    <path class="swoosh-rule" d="M212,324 L516,324 Q530,324 540,310 L586,244 Q594,232 608,232 L716,232"/>
    <circle class="arch" cx="157" cy="392" r="52"/>
    <circle class="arch" cx="603" cy="392" r="52"/>

    <circle class="logo-ring" cx="472" cy="220" r="64"/>
    <text class="logo-name" x="472" y="208" font-size="16">LARKIN</text>
    <text class="logo-name" x="472" y="226" font-size="12">THE</text>
    <text class="logo-name" x="472" y="244" font-size="16">PLUMBER</text>

    <g class="services">
      <circle class="bullet" cx="559" cy="162" r="3"/><text class="service" x="569" y="166">Blocked Drains</text>
      <circle class="bullet" cx="559" cy="176" r="3"/><text class="service" x="569" y="180">CCTV Inspections</text>
      <circle class="bullet" cx="559" cy="190" r="3"/><text class="service" x="569" y="194">Water Leaks</text>
      <circle class="bullet" cx="559" cy="204" r="3"/><text class="service" x="569" y="208">Hot Water Units</text>
      <circle class="bullet" cx="559" cy="218" r="3"/><text class="service" x="569" y="222">Gas Plumbing</text>
    </g>

    <text class="web-address" x="207" y="321" textLength="280" lengthAdjust="spacingAndGlyphs">WWW.LARKINTHEPLUMBER.COM.AU</text>
    <text class="slogan" x="630" y="276">NO JOB</text>
    <text class="slogan" x="630" y="299">TOO SMALL</text>

    <g class="phones">
      <text class="area-label" x="242" y="363">Gold Coast</text><text class="area-number" x="242" y="380">5550 2741</text>
      <line class="area-divider" x1="331" y1="352" x2="331" y2="382"/>
      <text class="area-label" x="343" y="363">Brisbane</text><text class="area-number" x="343" y="380">3700 6182</text>
      <line class="area-divider" x1="431" y1="352" x2="431" y2="382"/>
      <text class="area-label" x="444" y="363">Logan</text><text class="area-number" x="444" y="380">3400 9257</text>
    </g>
  </g>

  <!-- Front (bonnet) -->
  <g class="front">
    <path class="panel-white" d="M95,500 Q100,488 130,488 L330,488 Q360,488 365,500 L385,620 Q392,660 384,700 L378,770 L82,770 L76,700 Q68,660 75,620 Z"/>
    <ellipse class="logo-ring" cx="227" cy="620" rx="62" ry="22"/>
    <text class="logo-name" x="227" y="623" font-size="9">LARKIN THE PLUMBER</text>
  </g>

  <!-- Rear doors -->
  <g class="back">
    <path class="panel-white" d="M485,486 Q490,480 505,480 L658,480 Q672,480 677,488 L712,590 L720,690 L435,690 L443,590 Z"/>
    <rect class="panel-black" x="435" y="618" width="285" height="78"/>
    <rect x="476" y="620" width="112" height="36" rx="6" fill="var(--wrap-white)"/>
    <circle class="logo-ring" cx="528" cy="556" r="42"/>
    <text class="logo-name" x="528" y="549" font-size="11">LARKIN</text>
    <text class="logo-name" x="528" y="561" font-size="8">THE</text>
    <text class="logo-name" x="528" y="573" font-size="11">PLUMBER</text>
    <g class="services">
      <circle class="bullet" cx="586" cy="521" r="2.5"/><text class="service" x="594" y="524">Blocked Drains</text>
      <circle class="bullet" cx="586" cy="538" r="2.5"/><text class="service" x="594" y="541">CCTV Inspections</text>
      <circle class="bullet" cx="586" cy="555" r="2.5"/><text class="service" x="594" y="558">Water Leaks</text>
      <circle class="bullet" cx="586" cy="572" r="2.5"/><text class="service" x="594" y="575">Hot Water Units</text>
      <circle class="bullet" cx="586" cy="589" r="2.5"/><text class="service" x="594" y="592">Gas Plumbing</text>
    </g>
    <g class="phones">
      <text class="area-label" x="469" y="674">Gold Coast</text><text class="area-number" x="469" y="688">5550 2741</text>
      <line class="area-divider" x1="538" y1="665" x2="538" y2="690"/>
      <text class="area-label" x="546" y="674">Brisbane</text><text class="area-number" x="546" y="688">3700 6182</text>
      <line class="area-divider" x1="616" y1="665" x2="616" y2="690"/>
      <text class="area-label" x="624" y="674">Logan</text><text class="area-number" x="624" y="688">3400 9257</text>
    </g>
  </g>

  <!-- Side panel, passenger side (front at right) -->
  <g class="side side-right">
    <g transform="translate(790,722) scale(-1,1)">
      <path class="panel-white" d="M30,322 Q30,286 62,272 L172,236 Q232,190 302,160 Q324,148 362,146 L690,146 Q712,146 714,170 L718,395 L42,395 Q28,395 28,380 Z"/>
      <path class="panel-black" d="M212,334 L522,334 Q536,334 546,320 L592,254 Q600,242 614,242 L716,242 L718,395 L212,395 Z"/>
      <path class="swoosh-rule" d="M212,324 L516,324 Q530,324 540,310 L586,244 Q594,232 608,232 L716,232"/>
      <circle class="arch" cx="157" cy="392" r="52"/>
      <circle class="arch" cx="603" cy="392" r="52"/>
    </g>

    <circle class="logo-ring" cx="310" cy="946" r="64"/>
    <text class="logo-name" x="310" y="934" font-size="16">LARKIN</text>
    <text class="logo-name" x="310" y="952" font-size="12">THE</text>
    <text class="logo-name" x="310" y="970" font-size="16">PLUMBER</text>

    <g class="services">
      <circle class="bullet" cx="104" cy="885" r="3"/><text class="service" x="114" y="889">Blocked Drains</text>
      <circle class="bullet" cx="104" cy="899" r="3"/><text class="service" x="114" y="903">CCTV Inspections</text>
      <circle class="bullet" cx="104" cy="913" r="3"/><text class="service" x="114" y="917">Water Leaks</text>
      <circle class="bullet" cx="104" cy="927" r="3"/><text class="service" x="114" y="931">Hot Water Units</text>
      <circle class="bullet" cx="104" cy="941" r="3"/><text class="service" x="114" y="945">Gas Plumbing</text>
    </g>

    <text class="slogan" x="158" y="1001">NO JOB</text>
    <text class="slogan" x="158" y="1024">TOO SMALL</text>
    <text class="web-address" x="296" y="1043" textLength="280" lengthAdjust="spacingAndGlyphs">WWW.LARKINTHEPLUMBER.COM.AU</text>

    <g class="phones">
      <text class="area-label" x="265" y="1085">Gold Coast</text><text class="area-number" x="265" y="1102">5550 2741</text>
      <line class="area-divider" x1="354" y1="1074" x2="354" y2="1104"/>
      <text class="area-label" x="366" y="1085">Brisbane</text><text class="area-number" x="366" y="1102">3700 6182</text>
      <line class="area-divider" x1="454" y1="1074" x2="454" y2="1104"/>
      <text class="area-label" x="467" y="1085">Logan</text><text class="area-number" x="467" y="1102">3400 9257</text>
    </g>
  </g>
</svg>
</body>
</html>
```